ご提案ありがとうございました。赤系でシンプルなデザインであること、また、部内の10名以上で検討させていただき多票を獲得したので、多くの方にいい印象を与えるバナーであると判断し、採用を決めさせていただきました。試してみるの文言も良かったです。
皆さま、ご提案ありがとうございました。初めて利用させていただき、良い提案が多く迷いました。今後、またご依頼させていただく事もあるかと存じますので、その際にはまた、ご提案をよろしくお願いいたします。
【バナー2点募集!】求人サイト「RVTジョブリンク」へ誘導するバナーの作成 バナー作成の仕事の依頼
https://rvt-joblink.example/
栃木県に本社を持ち関東圏を中心にし総合人材サービス事業を展開しています。
製造系の人材派遣を中心に、人材紹介や業務請負、紹介予定派遣など幅広いサービスを提供しています。
社是「雇用創造」のもと「あらゆる人の雇用機会をつくり、あらゆる人の働く喜びをつくる。」
の経営理念を掲げダイバーシティ社会の実現に向け尽力しております。

```html
<!DOCTYPE html>
<html lang="ja">
<head>
<meta charset="utf-8">
<title>RVTジョブリンク 求人バナー</title>
<link rel="stylesheet" href="https://fonts.googleapis.com/css2?family=Noto+Sans+JP:wght@500;700;900&display=swap">
<style>
  :root {
    --red: #e8262b;
    --ink: #1a1a1a;
    --line: #9a9a9a;
    --paper: #ffffff;
    --photo-a: #d9dde2;
    --photo-b: #eef0f2;
  }
  * { margin: 0; padding: 0; box-sizing: border-box; }
  html, body { width: 1200px; height: 900px; overflow: hidden; background: var(--paper); }
  body { position: relative; font-family: "Noto Sans JP", sans-serif; color: var(--ink); }

  .banner { position: absolute; background: var(--paper); border: 2px solid var(--line); overflow: hidden; }
  .banner--wide { left: 36px; top: 36px; width: 568px; height: 250px; }
  .banner--large { left: 560px; top: 360px; width: 604px; height: 504px; }

  .photo { position: absolute; background: linear-gradient(180deg, var(--photo-b), var(--photo-a)); }

  .headline { position: absolute; font-weight: 900; line-height: 1; white-space: nowrap; }
  .headline .main { color: var(--red); }
  .headline .sub { color: var(--ink); }
  .search-line { position: absolute; font-weight: 700; white-space: nowrap; display: flex; align-items: center; gap: 4px; }

  .perk { background: var(--red); color: #fff; font-weight: 700; text-align: center; line-height: 1.15; display: flex; align-items: center; justify-content: center; }

  .tagline { position: absolute; font-weight: 700; line-height: 1.3; }
  .tagline em { font-style: normal; color: var(--red); }

  .brand { position: absolute; display: flex; align-items: center; gap: 10px; color: var(--red); font-weight: 900; white-space: nowrap; }
  .brand .mark { background: var(--red); display: block; }
</style>
</head>
<body>

<!-- Wide banner -->
<section class="banner banner--wide">
  <div class="photo" role="img" aria-label="スーツと作業服姿の笑顔の男女4名の写真" style="left:0;top:0;width:276px;height:186px;"></div>

  <div class="headline" style="left:284px;top:8px;font-size:46px;">
    <span class="main">工場・製造</span><span class="sub" style="font-size:26px;vertical-align:top;display:inline-block;line-height:1;">系<br>の</span>
  </div>
  <div class="search-line" style="left:286px;top:66px;font-size:27px;">
    求人情報を探すなら
    <svg width="22" height="22" viewBox="0 0 24 24" aria-hidden="true"><circle cx="10" cy="10" r="7" fill="none" stroke="#999" stroke-width="3"/><line x1="15" y1="15" x2="22" y2="22" stroke="#999" stroke-width="3.5" stroke-linecap="round"/></svg>
  </div>

  <div style="position:absolute;left:280px;top:112px;width:284px;height:64px;display:grid;grid-template-columns:repeat(4,1fr);gap:4px;">
    <div class="perk" style="font-size:20px;">寮<br>あり</div>
    <div class="perk" style="font-size:18px;">未経験<br>歓迎</div>
    <div class="perk" style="font-size:18px;">日払い<br>週払い</div>
    <div class="perk" style="font-size:20px;">土日<br>休み</div>
  </div>

  <p class="tagline" style="left:8px;top:192px;font-size:20px;">あなたの<em>条件</em>に<em>ピッタリ</em>の<br>仕事がきっと見つかる!</p>

  <div class="brand" style="left:292px;top:200px;font-size:30px;">
    <span class="mark" style="width:22px;height:22px;"></span>RVTジョブリンク
  </div>
</section>

<!-- Large banner -->
<section class="banner banner--large">
  <div style="position:absolute;left:0;top:0;width:98px;height:362px;background:var(--red);display:flex;flex-direction:column;">
    <div class="perk" style="flex:1;font-size:24px;border-bottom:2px solid #fff;">寮<br>あり</div>
    <div class="perk" style="flex:1;font-size:21px;border-bottom:2px solid #fff;">未経験<br>歓迎</div>
    <div class="perk" style="flex:1;font-size:21px;border-bottom:2px solid #fff;">日払い<br>週払い</div>
    <div class="perk" style="flex:1;font-size:24px;">土日<br>休み</div>
  </div>

  <div class="headline" style="left:112px;top:14px;font-size:62px;">
    <span class="main">工場・製造</span><span class="sub" style="font-size:34px;vertical-align:top;display:inline-block;line-height:1;">系<br>の</span>
  </div>
  <div class="search-line" style="left:114px;top:96px;font-size:36px;">
    求人情報を探すなら
    <svg width="30" height="30" viewBox="0 0 24 24" aria-hidden="true"><circle cx="10" cy="10" r="7" fill="none" stroke="#999" stroke-width="3"/><line x1="15" y1="15" x2="22" y2="22" stroke="#999" stroke-width="3.5" stroke-linecap="round"/></svg>
  </div>

  <div class="photo" role="img" aria-label="スーツと作業服姿の笑顔の男女4名の写真" style="left:98px;top:160px;width:506px;height:202px;"></div>

  <p class="tagline" style="left:0;top:372px;width:100%;text-align:center;font-size:24px;">あなたの<em>条件</em>に<em>ピッタリ</em>の仕事がきっと見つかる!</p>

  <div class="brand" style="left:0;width:100%;justify-content:center;top:418px;font-size:46px;">
    <span class="mark" style="width:32px;height:32px;"></span>RVTジョブリンク
  </div>
</section>

</body>
</html>
```